NEW Business Cards!
CNC Machine Shop Business Cards
Simple
Dale Workman
248 North Route 371
Kelvale, Texas 75418
WorkmanIronCraft@mailbox-example.com
www.WorkmanIronCraft.example
We also need this person on the same card somehow:
Travis Workman
Cell - 555.218.7730
Fax - Same
email - Same
In-House Services:
CNC Milling
CNC Turning
CNC Bending
Water Jet Cutting
Powder Coating

```html
<!DOCTYPE html>
<html lang="en">
<head>
<meta charset="utf-8">
<title>Workman Metal Works – Business Cards</title>
<link href="https://fonts.googleapis.com/css2?family=Source+Sans+3:wght@400;600;700&display=swap" rel="stylesheet">
<style>
  :root {
    --navy: #22207a;
    --blue: #1c8fd8;
    --gold: #b8935a;
    --ink: #2a2a86;
    --brown: #6b4a22;
    --paper: #ffffff;
    --stage: #ffffff;
    --border: #8a8a8a;
  }
  * { margin: 0; padding: 0; box-sizing: border-box; }
  html, body { width: 1200px; height: 742px; overflow: hidden; background: var(--stage); }
  body { position: relative; font-family: "Source Sans 3", "PT Sans", sans-serif; }

  .card { position: absolute; background: var(--paper); overflow: hidden; }
  .card--front { left: 38px; top: 19px; width: 560px; height: 336px; }
  .card--back-white { left: 610px; top: 36px; width: 554px; height: 324px; border: 2px solid var(--border); }
  .card--back-band { left: 288px; top: 372px; width: 569px; height: 360px; }

  .card__band { position: absolute; inset: 0; width: 100%; height: 100%; }

  .brand { position: absolute; display: flex; align-items: center; gap: 10px; white-space: nowrap; }
  .brand__mark { width: 40px; height: 40px; background: var(--blue); flex: none; }
  .brand__name { font-weight: 700; font-size: 24px; color: var(--navy); letter-spacing: 0.5px; line-height: 1; }

  .card--front .brand { left: 60px; top: 46px; }
  .card--back-white .brand { left: 100px; top: 58px; }
  .card--back-band .brand { left: 122px; top: 42px; }

  .people { position: absolute; left: 0; right: 0; top: 118px; text-align: center; color: var(--brown); font-size: 21px; line-height: 26px; }

  .contact { position: absolute; right: 18px; top: 224px; text-align: right; color: #fff; font-size: 14px; line-height: 19px; font-style: normal; }

  .services { position: absolute; left: 0; right: 0; top: 176px; text-align: center; color: var(--ink); font-size: 20px; line-height: 25px; }
  .services__title { font-weight: 700; margin-bottom: 24px; }

  .card--back-band .services__title { position: absolute; left: 0; right: 0; top: 136px; text-align: center; font-weight: 700; font-size: 20px; color: var(--ink); }
  .card--back-band .services__list { position: absolute; left: 0; right: 0; top: 236px; text-align: center; color: #fff; font-size: 20px; line-height: 25px; }
</style>
</head>
<body>

<section class="card card--front">
  <svg class="card__band" viewBox="0 0 560 336" preserveAspectRatio="none" aria-hidden="true">
    <defs>
      <linearGradient id="bandFront" x1="0" x2="1" y1="0" y2="0">
        <stop offset="0" stop-color="#1ea0e6"/>
        <stop offset="0.45" stop-color="#2a53b8"/>
        <stop offset="1" stop-color="#23207a"/>
      </linearGradient>
    </defs>
    <polygon points="0,214 560,168 560,336 0,336" fill="url(#bandFront)"/>
    <polygon points="0,206 560,158 560,164 0,212" fill="var(--gold)"/>
  </svg>
  <div class="brand"><span class="brand__mark"></span><span class="brand__name">WORKMAN METAL WORKS</span></div>
  <div class="people">
    <p class="person">Dale Workman</p>
    <p class="person">Travis Workman</p>
  </div>
  <address class="contact">
    248 North Route 371, Kelvale, Texas 75418<br>
    Dale Cell: 555.304.1186 | Fax: 555.671.2094<br>
    Travis Cell: 555.218.7730<br>
    Email: WorkmanIronCraft@mailbox-example.com<br>
    www.WorkmanIronCraft.example
  </address>
</section>

<section class="card card--back-white">
  <div class="brand"><span class="brand__mark"></span><span class="brand__name">WORKMAN METAL WORKS</span></div>
  <div class="services">
    <p class="services__title">In-House Services:</p>
    <p>CNC Milling, CNC Turning</p>
    <p>CNC Bending, Water Jet Cutting</p>
    <p>Powder Coating</p>
  </div>
</section>

<section class="card card--back-band">
  <svg class="card__band" viewBox="0 0 569 360" preserveAspectRatio="none" aria-hidden="true">
    <defs>
      <linearGradient id="bandBack" x1="0" x2="1" y1="0" y2="0">
        <stop offset="0" stop-color="#1ea0e6"/>
        <stop offset="0.45" stop-color="#2a53b8"/>
        <stop offset="1" stop-color="#23207a"/>
      </linearGradient>
    </defs>
    <polygon points="0,222 569,174 569,360 0,360" fill="url(#bandBack)"/>
    <polygon points="0,214 569,164 569,170 0,220" fill="var(--gold)"/>
  </svg>
  <div class="brand"><span class="brand__mark"></span><span class="brand__name">WORKMAN METAL WORKS</span></div>
  <p class="services__title">In-House Services:</p>
  <div class="services__list">
    <p>CNC Milling, CNC Turning</p>
    <p>CNC Bending, Water Jet Cutting</p>
    <p>Powder Coating</p>
  </div>
</section>

</body>
</html>
```